Business Recognition Design

We need a design for a recognition to be given to business leaders in our community.
The recognition shall be made on a brass plaque on wood panel background (picture attached, please use it as a background), and all drawing must be in vectors and only one color (black).
It should also have a logo on the top and signature on the right bottom.
The text is enclosed in DOC file.
Updates

Reason: just to be able to find the best solution

Reason: None of the suggestion is good enough. Logo in general is too big in comparison with the rest of the plate.

Industry/Entity Type

Business

Requirements
Must have
• - standard Windows font (or possibility to install the same font on Windows), as the name on the recognition shall be printed in the same font
Nice to have
• - some graphic element (in curves) representing achievements in business
- should look great :)

```html
<!DOCTYPE html>
<html lang="en">
<head>
<meta charset="utf-8">
<title>Business Recognition Plaque</title>
<link rel="stylesheet" href="https://fonts.googleapis.com/css2?family=Russo+One&family=Saira:wght@400;800&display=swap">
<style>
  :root {
    --wood-dark: #5a3418;
    --wood-mid: #7d4d2b;
    --wood-light: #94603a;
    --brass-deep: #b88f2c;
    --brass-mid: #d8b64c;
    --brass-light: #f4e08a;
    --ink: #0b0904;
    --ornament-dark: #4a3a10;
    --ornament-mid: #7a6020;
    --skin-light: #efd9a8;
    --skin-mid: #dcc089;
  }
  html, body {
    margin: 0;
    padding: 0;
    width: 1200px;
    height: 924px;
    overflow: hidden;
    background: var(--wood-mid);
  }
  .plaque {
    position: relative;
    width: 1200px;
    height: 924px;
    background: linear-gradient(180deg, var(--wood-light), var(--wood-mid) 45%, var(--wood-dark));
    font-family: "Saira", sans-serif;
    color: var(--ink);
  }
  .brass-plate {
    position: absolute;
    left: 50px;
    top: 52px;
    width: 1100px;
    height: 822px;
    background:
      repeating-linear-gradient(180deg, rgba(255,255,255,0.06) 0 2px, rgba(0,0,0,0.03) 2px 4px),
      linear-gradient(100deg, var(--brass-deep) 0%, var(--brass-mid) 30%, var(--brass-light) 65%, var(--brass-mid) 100%);
    box-shadow: 0 2px 6px rgba(0,0,0,0.45);
  }
  .plate-rule {
    position: absolute;
    inset: 4px;
    border: 2px solid var(--ink);
  }
  .ornament-border {
    position: absolute;
    left: 10px;
    top: 10px;
    right: 10px;
    bottom: 10px;
  }
  .ornament-border svg { display: block; }
  .hand-gesture {
    position: absolute;
    left: 834px;
    top: 246px;
    width: 220px;
    height: 358px;
    border-radius: 6px;
    background: linear-gradient(160deg, var(--skin-light), var(--skin-mid));
    opacity: 0.8;
  }
  .content > * { position: absolute; margin: 0; white-space: nowrap; }
  .logo-name {
    left: 76px;
    top: 94px;
    font-family: "Russo One", sans-serif;
    font-size: 88px;
    line-height: 1;
    letter-spacing: 1px;
  }
  .title-box {
    left: 76px;
    top: 252px;
    height: 87px;
    width: 436px;
    padding-left: 38px;
    border: 4.5px solid var(--ink);
    border-radius: 34px;
    font-weight: 400;
    font-size: 56px;
    line-height: 87px;
    letter-spacing: 0;
  }
  .award-line {
    left: 76px;
    font-size: 39px;
    line-height: 1;
    letter-spacing: 1.6px;
  }
  .award-title { top: 396px; }
  .award-recipient { top: 452px; }
  .recipient-name { font-weight: 800; letter-spacing: 1.8px; }
  .citation {
    left: 76px;
    top: 532px;
    font-size: 28px;
    line-height: 41.6px;
    letter-spacing: 1.2px;
  }
  .company-name { font-weight: 800; }
  .footer-line {
    top: 718px;
    font-size: 28px;
    line-height: 1;
    letter-spacing: 1.2px;
  }
  .award-date { left: 76px; }
  .award-date sup { font-size: 15px; }
  .signatory { left: 595px; }
</style>
</head>
<body>
<div class="plaque">
  <div class="brass-plate">
    <div class="plate-rule"></div>
    <div class="ornament-border" role="img" aria-label="Decorative black floral ornament border around the plate">
      <svg width="1080" height="802" viewBox="0 0 1080 802">
        <defs>
          <linearGradient id="ornamentTone" x1="0" y1="0" x2="1" y2="0">
            <stop offset="0" stop-color="var(--ornament-dark)"/>
            <stop offset="0.6" stop-color="var(--ornament-mid)"/>
            <stop offset="1" stop-color="var(--ornament-dark)"/>
          </linearGradient>
        </defs>
        <path fill-rule="evenodd" fill="url(#ornamentTone)" d="M0 0H1080V802H0Z M44 44V758H1036V44Z"/>
        <rect x="1" y="1" width="1078" height="800" fill="none" stroke="var(--ink)" stroke-width="2"/>
        <rect x="44" y="44" width="992" height="714" fill="none" stroke="var(--ink)" stroke-width="1.5"/>
      </svg>
    </div>
    <div class="hand-gesture" role="img" aria-label="Photograph of a hand giving a thumbs-up"></div>
    <div class="content">
      <p class="logo-name">(Our Logo)</p>
      <p class="title-box">RECOGNITION</p>
      <p class="award-line award-title">The Best Entrepreneur in 2013</p>
      <p class="award-line award-recipient">to Mr. <span class="recipient-name">Daniel R. Whitford</span>, MBA</p>
      <p class="citation">Under the leadership of Mr. Daniel R. Whitford, MBA<br>the company <span class="company-name">DR-WHITFORD Ltd</span> has been selected<br>by a City Council as the best company of The City.</p>
      <p class="footer-line award-date">Date: 4<sup>th</sup> July, 2013</p>
      <p class="footer-line signatory">City Mayor</p>
    </div>
  </div>
</div>
</body>
</html>
```